E-mail newsletter design - tolvexcraft

We are a gaming app developer

When an in-app game finishes, we would like to mail people taking part in leagues with a table showing where they finished along with all other players.

There could be up to 20 players in each league.

The mail shows the name of the league they are in and has an announcement regarding the game currently going on.

The mail should be HTML formatted and follow the look and feel of our website

Mail should be branded based on which app is sending the mail
tolvex startline - see tolvexstartline.example
tolvex scrumba - see tolvexscrumba.example
tolvex quizzle see tolvexquizzle.example

It should include a graphic element that is able to be written over, containing the placeholder text "Don't forget to play (name of next game) starting on (date)"

Requirements
Must have
• Any graphical elements should be provided separately

```html
<!DOCTYPE html>
<html lang="en">
<head>
<meta charset="utf-8">
<title>League Ladder Mailers</title>
<link href="https://fonts.googleapis.com/css2?family=Arimo:wght@400;700&display=swap" rel="stylesheet">
<style>
:root{
  --page:#ffffff;
  --brand-blue:#2d5d88;
  --card:#f7f8fa;
  --rule:#c3141f;
  --bar:#3a6f9f;
  --bar-shadow:#1e4566;
  --ink:#111111;
  --link:#1a1aa6;
}
*{box-sizing:border-box;margin:0;padding:0}
html,body{width:1200px;height:628px;overflow:hidden;background:var(--page)}
body{font-family:"Arimo",Arial,sans-serif;color:var(--ink)}
.mailers{display:flex;gap:18px;padding:30px 0 0 6px}
.mailer{width:360px}
.mailer-frame{position:relative;height:496px;background:var(--brand-blue)}
.brand{height:86px;display:flex;align-items:center;justify-content:center;gap:8px}
.brand-dot{width:14px;height:14px;border-radius:50%;background:#ffffff}
.brand-name{color:#ffffff;font-weight:700;font-size:17px;letter-spacing:.2px}
.card{position:absolute;left:17px;top:86px;width:327px;height:392px;background:var(--card);padding:10px 16px 0}
.sender{font-size:7px;font-weight:700}
.league-title{font-size:7px;font-weight:700;margin-top:11px}
.ladder{margin-top:14px;width:295px;border-collapse:collapse;font-size:7px}
.ladder th,.ladder td{border:1.5px solid var(--rule);height:16px;padding:0 3px;text-align:left}
.ladder th{font-weight:700}
.ladder td{font-weight:400}
.ladder .col-pos{width:82px}
.ladder .col-name{width:145px}
.reminder{position:absolute;left:0;top:478px;width:360px;height:16px;background:var(--bar);box-shadow:0 2px 2px var(--bar-shadow);display:flex;align-items:center;padding-left:10px;color:#ffffff;font-size:7.5px;font-weight:700;letter-spacing:.3px}
.reminder-item{display:flex;align-items:center;gap:4px}
.reminder-item + .reminder-item{margin-left:26px}
.reminder svg{width:10px;height:10px}
.legal{text-align:center;font-size:6px;margin-top:12px;line-height:16px}
.legal a{color:var(--link)}
</style>
</head>
<body>
<main class="mailers">

  <section class="mailer">
    <div class="mailer-frame">
      <header class="brand"><span class="brand-dot"></span><span class="brand-name">tolvex startline</span></header>
      <div class="card">
        <p class="sender">FROM: Tolvexstartline</p>
        <p class="league-title">League Ladder for Besy League ever</p>
        <table class="ladder">
          <tr><th class="col-pos">POSITION</th><th class="col-name">NAME</th><th>POINTS</th></tr>
          <tr><td>1</td><td>Jonah Reeve</td><td>3519</td></tr>
          <tr><td>2</td><td>Tobin Stace</td><td>2408</td></tr>
          <tr><td>3</td><td>Corin Hollow</td><td>1956</td></tr>
          <tr><td>4</td><td>Annika Dell</td><td>1813</td></tr>
          <tr><td>5</td><td>Callum Mendes</td><td>486</td></tr>
          <tr><td>6</td><td>Tomas Engberg</td><td>153</td></tr>
          <tr><td>7</td><td>Ollie Carden</td><td>-130</td></tr>
          <tr><td>8</td><td>Manesh Crickley</td><td>-323</td></tr>
          <tr><td>9</td><td>Adel Ibarra</td><td>-577</td></tr>
          <tr><td>10</td><td>Bram Turlow</td><td>-1672</td></tr>
          <tr><td>11</td><td>xxxxxxx</td><td>xxxx</td></tr>
          <tr><td>12</td><td>xxxxxxx</td><td>xxxx</td></tr>
          <tr><td>13</td><td>xxxxxxx</td><td>xxxx</td></tr>
          <tr><td>14</td><td>xxxxxxx</td><td>xxxx</td></tr>
          <tr><td>15</td><td>xxxxxxx</td><td>xxxx</td></tr>
          <tr><td>16</td><td>xxxxxxx</td><td>xxxx</td></tr>
          <tr><td>17</td><td>xxxxxxx</td><td>xxxx</td></tr>
          <tr><td>18</td><td>xxxxxxx</td><td>xxxx</td></tr>
          <tr><td>19</td><td>xxxxxxx</td><td>xxxx</td></tr>
          <tr><td>20</td><td>xxxxxxx</td><td>xxxx</td></tr>
        </table>
      </div>
      <div class="reminder">
        <span class="reminder-item"><svg viewBox="0 0 10 10"><circle cx="5" cy="5" r="4.3" fill="none" stroke="#fff" stroke-width="1"/><path d="M4 3v4l3-2z" fill="#fff"/></svg>DON'T FORGET TO PLAY ▸ &nbsp;XXXXX GAME</span>
        <span class="reminder-item"><svg viewBox="0 0 10 10"><circle cx="5" cy="5" r="4.3" fill="none" stroke="#fff" stroke-width="1"/><path d="M4 3v4l3-2z" fill="#fff"/></svg>STARTING ON ▸ &nbsp;0X-0X-2012</span>
      </div>
    </div>
    <footer class="legal">
      <p>Use of this Web site constitutes acceptance of tolvexcraft's <a href="#">Terms of Service</a> and <a href="#">Privacy Policy</a></p>
      <p>© Copyright 2012 Brasswick Systems Ltd. All rights reserved.</p>
    </footer>
  </section>

  <section class="mailer">
    <div class="mailer-frame">
      <header class="brand"><span class="brand-dot"></span><span class="brand-name">tolvex scrumba</span></header>
      <div class="card">
        <p class="sender">FROM: Tolvexstartline</p>
        <p class="league-title">League Ladder for Besy League ever</p>
        <table class="ladder">
          <tr><th class="col-pos">POSITION</th><th class="col-name">NAME</th><th>POINTS</th></tr>
          <tr><td>1</td><td>Jonah Reeve</td><td>3519</td></tr>
          <tr><td>2</td><td>Tobin Stace</td><td>2408</td></tr>
          <tr><td>3</td><td>Corin Hollow</td><td>1956</td></tr>
          <tr><td>4</td><td>Annika Dell</td><td>1813</td></tr>
          <tr><td>5</td><td>Callum Mendes</td><td>486</td></tr>
          <tr><td>6</td><td>Tomas Engberg</td><td>153</td></tr>
          <tr><td>7</td><td>Ollie Carden</td><td>-130</td></tr>
          <tr><td>8</td><td>Manesh Crickley</td><td>-323</td></tr>
          <tr><td>9</td><td>Adel Ibarra</td><td>-577</td></tr>
          <tr><td>10</td><td>Bram Turlow</td><td>-1672</td></tr>
          <tr><td>11</td><td>xxxxxxx</td><td>xxxx</td></tr>
          <tr><td>12</td><td>xxxxxxx</td><td>xxxx</td></tr>
          <tr><td>13</td><td>xxxxxxx</td><td>xxxx</td></tr>
          <tr><td>14</td><td>xxxxxxx</td><td>xxxx</td></tr>
          <tr><td>15</td><td>xxxxxxx</td><td>xxxx</td></tr>
          <tr><td>16</td><td>xxxxxxx</td><td>xxxx</td></tr>
          <tr><td>17</td><td>xxxxxxx</td><td>xxxx</td></tr>
          <tr><td>18</td><td>xxxxxxx</td><td>xxxx</td></tr>
          <tr><td>19</td><td>xxxxxxx</td><td>xxxx</td></tr>
          <tr><td>20</td><td>xxxxxxx</td><td>xxxx</td></tr>
        </table>
      </div>
      <div class="reminder">
        <span class="reminder-item"><svg viewBox="0 0 10 10"><circle cx="5" cy="5" r="4.3" fill="none" stroke="#fff" stroke-width="1"/><path d="M4 3v4l3-2z" fill="#fff"/></svg>DON'T FORGET TO PLAY ▸ &nbsp;XXXXX GAME</span>
        <span class="reminder-item"><svg viewBox="0 0 10 10"><circle cx="5" cy="5" r="4.3" fill="none" stroke="#fff" stroke-width="1"/><path d="M4 3v4l3-2z" fill="#fff"/></svg>STARTING ON ▸ &nbsp;0X-0X-2012</span>
      </div>
    </div>
    <footer class="legal">
      <p>Use of this Web site constitutes acceptance of tolvexcraft's <a href="#">Terms of Service</a> and <a href="#">Privacy Policy</a></p>
      <p>© Copyright 2012 Brasswick Systems Ltd. All rights reserved.</p>
    </footer>
  </section>

  <section class="mailer">
    <div class="mailer-frame">
      <header class="brand"><span class="brand-dot"></span><span class="brand-name">tolvex showcase</span></header>
      <div class="card">
        <p class="sender">FROM: Tolvexstartline</p>
        <p class="league-title">League Ladder for Besy League ever</p>
        <table class="ladder">
          <tr><th class="col-pos">POSITION</th><th class="col-name">NAME</th><th>POINTS</th></tr>
          <tr><td>1</td><td>Jonah Reeve</td><td>3519</td></tr>
          <tr><td>2</td><td>Tobin Stace</td><td>2408</td></tr>
          <tr><td>3</td><td>Corin Hollow</td><td>1956</td></tr>
          <tr><td>4</td><td>Annika Dell</td><td>1813</td></tr>
          <tr><td>5</td><td>Callum Mendes</td><td>486</td></tr>
          <tr><td>6</td><td>Tomas Engberg</td><td>153</td></tr>
          <tr><td>7</td><td>Ollie Carden</td><td>-130</td></tr>
          <tr><td>8</td><td>Manesh Crickley</td><td>-323</td></tr>
          <tr><td>9</td><td>Adel Ibarra</td><td>-577</td></tr>
          <tr><td>10</td><td>Bram Turlow</td><td>-1672</td></tr>
          <tr><td>11</td><td>xxxxxxx</td><td>xxxx</td></tr>
          <tr><td>12</td><td>xxxxxxx</td><td>xxxx</td></tr>
          <tr><td>13</td><td>xxxxxxx</td><td>xxxx</td></tr>
          <tr><td>14</td><td>xxxxxxx</td><td>xxxx</td></tr>
          <tr><td>15</td><td>xxxxxxx</td><td>xxxx</td></tr>
          <tr><td>16</td><td>xxxxxxx</td><td>xxxx</td></tr>
          <tr><td>17</td><td>xxxxxxx</td><td>xxxx</td></tr>
          <tr><td>18</td><td>xxxxxxx</td><td>xxxx</td></tr>
          <tr><td>19</td><td>xxxxxxx</td><td>xxxx</td></tr>
          <tr><td>20</td><td>xxxxxxx</td><td>xxxx</td></tr>
        </table>
      </div>
      <div class="reminder">
        <span class="reminder-item"><svg viewBox="0 0 10 10"><circle cx="5" cy="5" r="4.3" fill="none" stroke="#fff" stroke-width="1"/><path d="M4 3v4l3-2z" fill="#fff"/></svg>DON'T FORGET TO PLAY ▸ &nbsp;XXXXX GAME</span>
        <span class="reminder-item"><svg viewBox="0 0 10 10"><circle cx="5" cy="5" r="4.3" fill="none" stroke="#fff" stroke-width="1"/><path d="M4 3v4l3-2z" fill="#fff"/></svg>STARTING ON ▸ &nbsp;0X-0X-2012</span>
      </div>
    </div>
    <footer class="legal">
      <p>Use of this Web site constitutes acceptance of tolvexcraft's <a href="#">Terms of Service</a> and <a href="#">Privacy Policy</a></p>
      <p>© Copyright 2012 Brasswick Systems Ltd. All rights reserved.</p>
    </footer>
  </section>

</main>
</body>
</html>
```